Label for a new chocolate snack

Hello. We are Meadow Sweets Store. We are a new company making healthy chocolate snacks. We need Labels for our first product: Orla's Chocolate Figs,

We have two varieties:

1) dark chocolate

2) milk chocolate

The labels are 4 inches wide by 6 inches height. They are being printed on white glossy paper. They will be going on Kraft bags.

Here is the info we need on the labels:

Orla's
Chocolate Dates
Peanut Butter Center
Milk Chocolate
8g of Protein
Great Source of Energy
175g.

Orlas Chocolate Figs are targeted towards women who are 20-45 years of age.
Our goal is to create products that are healthy and taste good at the same time.

Finally, we will be adding more variations in the future, such as almond butter center, so being able to change the theme of the label to match the center filling would be good.

Thank you to everyone who will be submitting a design and good luck.

Target Market(s)

Woman, 20-40 years old, shop at gourmet grocery stores and health food stores

Industry/Entity Type

It Company

Colors

Designer to choose colors to be used in the design.

Requirements
Must have
• Orla's
• Chocolate Dates
• Peanut Butter Centre
• Milk Chocolate / Dark Chocolate
• 8g of Protein
• Great Source of Energy
• 175g.
• Back side of label must have everything contained in the pdfs i have attached.
• We are looking for a upscale chocolate look. That will still stand out on the shelf.
Should not have
• Main colors should not be brown, or black.

```html
<!DOCTYPE html>
<html lang="en">
<head>
<meta charset="utf-8">
<title>Orla's Chocolate Dates – Dark Chocolate Label</title>
<link rel="stylesheet" href="https://fonts.googleapis.com/css2?family=Dosis:wght@300;400;500;600&family=Source+Sans+3:wght@400;600&display=swap">
<style>
  :root {
    --cream: #fbf0c9;
    --red: #c1272d;
    --deep-brown: #6e2d1c;
    --badge-brown: #7a3a22;
    --white: #ffffff;
    --text-dark: #3a2a22;
  }
  * { margin: 0; padding: 0; box-sizing: border-box; }
  html, body { width: 800px; height: 1200px; overflow: hidden; background: var(--cream); }
  .label {
    position: relative;
    width: 800px;
    height: 1200px;
    background: var(--cream);
    font-family: "Dosis", sans-serif;
    overflow: hidden;
  }
  .corner-flag { position: absolute; left: 0; top: 0; width: 320px; height: 320px; }
  .brand {
    position: absolute; top: 72px; left: 0; width: 100%;
    text-align: center;
    font-family: "Dosis", sans-serif;
    font-weight: 500;
    font-size: 84px;
    line-height: 1.2;
    color: var(--deep-brown);
    letter-spacing: 1px;
  }
  .product-line1 {
    position: absolute; top: 252px; left: 0; width: 100%;
    text-align: center;
    font-weight: 500;
    font-size: 90px;
    line-height: 1;
    color: var(--red);
    letter-spacing: 1px;
  }
  .product-line2 {
    position: absolute; top: 340px; left: 0; width: 100%;
    text-align: center;
    font-weight: 400;
    font-size: 142px;
    line-height: 1;
    color: var(--red);
    letter-spacing: 3px;
  }
  .variety-ribbon { position: absolute; left: 196px; top: 518px; width: 410px; height: 60px; }
  .hero-visual {
    position: absolute; left: 26px; top: 636px; width: 640px; height: 430px;
    border-radius: 46% 54% 40% 48% / 52% 44% 56% 48%;
    background: radial-gradient(ellipse at 55% 35%, #5a2a22 0%, #3d1a16 45%, #2a1512 70%, rgba(42,21,18,0) 100%),
                radial-gradient(ellipse at 62% 78%, #d39a55 0%, rgba(211,154,85,0) 40%);
    opacity: 0.92;
  }
  .protein-badge { position: absolute; left: 668px; top: 890px; width: 100px; height: 130px; }
  .energy-badge { position: absolute; left: 648px; top: 1044px; width: 140px; height: 140px; overflow: visible; }
  .net-weight {
    position: absolute; top: 1128px; left: 0; width: 100%;
    text-align: center;
    font-family: "Source Sans 3", sans-serif;
    font-size: 28px;
    color: var(--text-dark);
  }
</style>
</head>
<body>
<main class="label">
  <svg class="corner-flag" viewBox="0 0 320 320" aria-label="Peanut Butter Center">
    <polygon points="0,0 308,0 0,308" fill="var(--red)"/>
    <g transform="translate(118,118) rotate(-45)" fill="var(--white)" font-family="Dosis, sans-serif" font-weight="500" font-size="30" text-anchor="middle" letter-spacing="1">
      <text x="0" y="-8">PEANUT</text>
      <text x="0" y="28">BUTTER CENTER</text>
    </g>
  </svg>

  <h1 class="brand">Orla's</h1>
  <p class="product-line1">CHOCOLATE</p>
  <p class="product-line2">DATES</p>

  <svg class="variety-ribbon" viewBox="0 0 410 60" aria-label="Dark Chocolate">
    <polygon points="0,0 410,0 392,30 410,60 0,60 18,30" fill="var(--red)"/>
    <text x="205" y="41" text-anchor="middle" fill="var(--white)" font-family="Dosis, sans-serif" font-weight="600" font-size="32" letter-spacing="1.5">DARK CHOCOLATE</text>
  </svg>

  <div class="hero-visual" role="img" aria-label="Pile of whole dates with dark chocolate squares and a swirl of peanut butter"></div>

  <svg class="protein-badge" viewBox="0 0 100 130" aria-label="8g of protein">
    <circle cx="50" cy="50" r="43" fill="none" stroke="var(--badge-brown)" stroke-width="3.5"/>
    <text x="50" y="66" text-anchor="middle" fill="var(--badge-brown)" font-family="Dosis, sans-serif" font-weight="500" font-size="44">8g</text>
    <text x="50" y="116" text-anchor="middle" fill="var(--badge-brown)" font-family="Dosis, sans-serif" font-weight="500" font-size="15">OF PROTEIN</text>
  </svg>

  <svg class="energy-badge" viewBox="0 0 140 140" aria-label="Great source of energy">
    <defs>
      <path id="energy-arc" d="M 21,98 A 56,56 0 1 1 119,98"/>
    </defs>
    <circle cx="70" cy="70" r="66" fill="none" stroke="var(--badge-brown)" stroke-width="3"/>
    <text fill="var(--badge-brown)" font-family="Dosis, sans-serif" font-weight="500" font-size="14" letter-spacing="0.5">
      <textPath href="#energy-arc" startOffset="50%" text-anchor="middle">GREAT SOURCE OF ENERGY</textPath>
    </text>
    <circle cx="70" cy="84" r="22" fill="var(--badge-brown)" role="img" aria-label="Runner icon"/>
  </svg>

  <p class="net-weight">Net Wt.175g</p>
</main>
</body>
</html>
```